brolvix new business card design project

we need a new business card design. you can view info about us @ brolvix.example. i have attached an example of our previous card with our previous name that we no longer use. We really liked the design, colors etc. look below to see more info about this project. it asks for a limited number of words. please see our website for more info about our compnay.

Target Market(s)

law enforcement

Contact Information for Business Card

i have uploaded an example of what we used before that we liked.

Font styles to use
Serif

```html
<!DOCTYPE html>
<html lang="en">
<head>
<meta charset="utf-8">
<title>Brolvix Business Card</title>
<link href="https://fonts.googleapis.com/css2?family=Source+Sans+3:wght@400;600&display=swap" rel="stylesheet">
<style>
  :root {
    --page: #ececec;
    --card: #2a2a2a;
    --brand-blue: #5574b8;
    --brand-light: #9aa8d8;
    --text-light: #e6e6e6;
    --band-gray: #4a4849;
    --divider: #5a5a5a;
  }
  html, body {
    margin: 0;
    width: 1200px;
    height: 1200px;
    overflow: hidden;
    background: var(--page);
    font-family: "Source Sans 3", sans-serif;
  }
  .card {
    position: absolute;
    left: 250px;
    width: 700px;
    height: 400px;
    background: var(--card);
    box-shadow: 0 6px 18px rgba(0,0,0,0.18);
    overflow: hidden;
  }
  .card-front { top: 130px; }
  .card-back { top: 620px; }

  .wordmark {
    position: absolute;
    left: 0;
    right: 0;
    text-align: center;
    color: var(--brand-light);
    font-weight: 600;
    letter-spacing: 6px;
    margin: 0;
  }
  .card-front .wordmark { top: 158px; font-size: 72px; line-height: 84px; }
  .card-back .wordmark { top: 70px; font-size: 60px; line-height: 70px; }

  .identity {
    position: absolute;
    top: 180px;
    right: 372px;
    text-align: right;
    color: var(--text-light);
    font-size: 17px;
    line-height: 22px;
  }
  .identity .person-name {
    color: var(--brand-blue);
    font-weight: 600;
    font-size: 21px;
    line-height: 26px;
  }
  .divider {
    position: absolute;
    left: 344px;
    top: 176px;
    width: 1px;
    height: 80px;
    background: var(--divider);
  }
  .contacts {
    position: absolute;
    top: 180px;
    left: 360px;
    margin: 0;
    padding: 0;
    list-style: none;
    color: var(--text-light);
    font-size: 17px;
    line-height: 24px;
  }
  .contacts li { display: flex; align-items: center; gap: 8px; }
  .contacts svg { width: 13px; height: 13px; fill: none; stroke: var(--text-light); stroke-width: 1.6; }
  .contacts .phone-icon { fill: var(--text-light); stroke: none; }
  .address {
    position: absolute;
    top: 290px;
    left: 0;
    right: 0;
    text-align: center;
    color: var(--text-light);
    font-size: 17px;
  }
  .bottom-band {
    position: absolute;
    left: 0;
    bottom: 0;
    width: 700px;
    height: 20px;
  }
</style>
</head>
<body>
  <section class="card card-front">
    <p class="wordmark">BROLVIX</p>
  </section>

  <section class="card card-back">
    <p class="wordmark">BROLVIX</p>

    <div class="identity">
      <div class="person-name">Dorian Maxfield</div>
      <div>Founder</div>
      <div>Chief Executive Officer</div>
    </div>

    <div class="divider"></div>

    <ul class="contacts">
      <li>
        <svg viewBox="0 0 16 16"><path class="phone-icon" d="M4 1l3 3-2 2c1 2 3 4 5 5l2-2 3 3-2 2C7 14 2 9 1 3z"/></svg>
        555.201.4470
      </li>
      <li>
        <svg viewBox="0 0 16 16"><rect x="1.5" y="3.5" width="13" height="9"/><path d="M1.5 3.5l6.5 5 6.5-5"/></svg>
        info@brolvix.example
      </li>
      <li>
        <svg viewBox="0 0 16 16"><circle cx="8" cy="8" r="6.5"/><ellipse cx="8" cy="8" rx="3" ry="6.5"/><path d="M1.5 8h13"/></svg>
        brolvix.example
      </li>
    </ul>

    <p class="address">4120 Larkspur Avenue, Fairhaven, TX 75990</p>

    <svg class="bottom-band" viewBox="0 0 700 20" aria-hidden="true">
      <polygon points="0,0 410,0 400,20 0,20" fill="var(--brand-blue)"/>
      <polygon points="410,0 700,0 700,20 400,20" fill="var(--band-gray)"/>
    </svg>
  </section>
</body>
</html>
```